TIDAL VERGE needs bisness cards pronto

Bisness name is "TIDAL VERGE" new bisness the bisness includes lawn mowing, garden matanace, and any jobs around the house.
I need a card that is colorful and vibrant and the bisness of lawn mowing maybe with some nature with it. It also needs my contact details"Darren Quellby mobile 0413562049 call for free quote and email norma.vance@fernmail.com.au and a catchy tag line

Industry/Entity Type

House

Requirements
Must have
• Bisness name "TIDAL VERGE"
Contact details "0413562049"
Email norma.vance@fernmail.com.au
Call for free quote

```html
<!DOCTYPE html>
<html lang="en">
<head>
<meta charset="utf-8">
<title>Tidal Verge – Business Card</title>
<link rel="stylesheet" href="https://fonts.googleapis.com/css2?family=Signika:wght@300;400;600&display=swap">
<style>
  :root {
    --page-bg: #f4f4f4;
    --charcoal: #3f3b3a;
    --mist: #dcdddf;
    --leaf: #a6cf42;
    --text-light: #e8e8e8;
  }
  html, body {
    margin: 0;
    padding: 0;
    width: 1200px;
    height: 1000px;
    overflow: hidden;
    background: var(--page-bg);
  }
  .card {
    position: absolute;
    left: 114px;
    top: 203px;
    width: 973px;
    height: 594px;
    background: var(--mist);
    font-family: "Signika", sans-serif;
    overflow: hidden;
  }
  .card__contact {
    position: absolute;
    left: 0;
    top: 0;
    width: 664px;
    height: 594px;
    background: var(--charcoal);
    color: var(--text-light);
  }
  .contact-block {
    position: absolute;
    right: 23px;
    top: 156px;
    text-align: right;
    font-weight: 300;
    font-size: 38px;
    line-height: 37px;
  }
  .contact-block p { margin: 0; white-space: nowrap; }
  .contact-name { margin-bottom: 33px !important; font-weight: 300; }
  .contact-value { font-weight: 600; }
  .contact-gap { margin-top: 16px !important; }
  .tagline {
    position: absolute;
    right: 23px;
    bottom: 40px;
    margin: 0;
    font-size: 26px;
    font-weight: 300;
    color: var(--leaf);
    white-space: nowrap;
  }
  .card__accents {
    position: absolute;
    left: 664px;
    top: 0;
    width: 168px;
    height: 594px;
    background: linear-gradient(90deg, rgba(166,207,66,0.75) 0%, rgba(166,207,66,0.35) 55%, rgba(166,207,66,0) 100%);
  }
  .brand-mark {
    position: absolute;
    left: 866px;
    top: 86px;
    width: 30px;
    height: 30px;
    background: var(--charcoal);
  }
  .brand-name {
    position: absolute;
    left: 866px;
    top: 168px;
    writing-mode: vertical-rl;
    font-size: 46px;
    font-weight: 300;
    letter-spacing: 4px;
    color: var(--charcoal);
    line-height: 1;
    white-space: nowrap;
  }
</style>
</head>
<body>
  <div class="card">
    <section class="card__contact">
      <div class="contact-block">
        <p class="contact-name">Darren Quellby</p>
        <p>mobile</p>
        <p class="contact-value">0413562049</p>
        <p>call for free quote</p>
        <p class="contact-gap">email</p>
        <p class="contact-value">norma.vance@fernmail.com.au</p>
      </div>
      <p class="tagline">Sharp edges, happy homes</p>
    </section>

    <div class="card__accents" role="img" aria-label="Scattered green leaf shard decoration"></div>

    <div class="brand-mark" aria-hidden="true"></div>
    <div class="brand-name">TIDAL VERGE</div>
  </div>
</body>
</html>
```